I need a design for Brightmoor Homes which is a custom home builder. The name on it will be Dan Porter, and I will give the phone number to the winning design. No address or website needed.

```html
<!DOCTYPE html>
<html lang="en">
<head>
<meta charset="utf-8">
<title>Brightmoor Homes – Business Card</title>
<link href="https://fonts.googleapis.com/css2?family=Tinos:wght@700&display=swap" rel="stylesheet">
<style>
  :root {
    --page: #ffffff;
    --card-blue: #00aeef;
    --band-blue: #1b8fc9;
    --ink: #000000;
    --strip: #1a1a1a;
    --white: #ffffff;
    --skyline-top: #4a4a4a;
    --skyline-bottom: #1e1e1e;
    --mark: #1d2f8f;
  }
  * { box-sizing: border-box; margin: 0; padding: 0; }
  html, body {
    width: 1200px; height: 848px; overflow: hidden;
    background: var(--page);
    font-family: "Tinos", "Times New Roman", serif;
    font-weight: 700;
  }
  .sheet { position: relative; width: 1200px; height: 848px; }
  .side-label {
    position: absolute; top: 292px; width: 362px;
    text-align: center; font-size: 37px; color: var(--ink); line-height: 1;
  }
  .side-label--front { left: 208px; }
  .side-label--back { left: 586px; }
  .card {
    position: absolute; top: 335px; width: 358px; height: 207px;
    background: var(--card-blue); overflow: hidden;
  }
  .card--front { left: 208px; }
  .card--back { left: 586px; }
  .title-strip {
    position: absolute; left: 0; top: 0; width: 23px; height: 185px;
    background: linear-gradient(to right, var(--ink), var(--strip) 70%, #555);
    display: flex; flex-direction: column; align-items: center;
    padding-top: 30px; color: var(--white); font-size: 11px; line-height: 11.8px;
  }
  .phone {
    position: absolute; right: 7px; top: 4px;
    font-size: 7px; color: var(--white);
  }
  .identity {
    position: absolute; left: 23px; right: 0; top: 66px;
    text-align: center; color: var(--white); line-height: 1.05;
  }
  .identity__role { font-size: 21px; margin-left: 8px; }
  .identity__name { font-size: 26px; margin-left: 4px; }
  .skyline {
    position: absolute; left: 23px; right: 0; top: 124px; height: 61px;
    background: linear-gradient(to bottom, rgba(74,74,74,0) 0%, var(--skyline-top) 45%, var(--skyline-bottom) 100%);
  }
  .band {
    position: absolute; left: 0; right: 0; bottom: 0; height: 22px;
    background: var(--band-blue);
    border-top: 2px solid var(--ink); border-bottom: 4px solid var(--ink);
  }
  .brand {
    position: absolute; left: 0; right: 0; top: 30px;
    display: flex; flex-direction: column; align-items: center;
  }
  .brand__square {
    width: 80px; height: 80px; background: var(--mark);
    margin-bottom: 30px;
  }
  .brand__name {
    color: var(--white); font-size: 26px; line-height: 1; white-space: nowrap;
  }
</style>
</head>
<body>
<main class="sheet">
  <h2 class="side-label side-label--front">FRONT</h2>
  <h2 class="side-label side-label--back">BACK</h2>

  <section class="card card--front">
    <div class="title-strip" aria-label="Home Builder">
      <span>H</span><span>o</span><span>m</span><span>e</span><span>&nbsp;</span>
      <span>B</span><span>u</span><span>i</span><span>l</span><span>d</span><span>e</span><span>r</span>
    </div>
    <p class="phone">Phone Number 0000000000</p>
    <div class="identity">
      <p class="identity__role">Home Builder</p>
      <p class="identity__name">Dan Porter</p>
    </div>
    <div class="skyline" role="img" aria-label="City skyline silhouette with bridge, towers and domes"></div>
    <div class="band" role="img" aria-label="Decorative chevron border band"></div>
  </section>

  <section class="card card--back">
    <div class="brand">
      <div class="brand__square"></div>
      <p class="brand__name">BRIGHTMOOR HOMES</p>
    </div>
    <div class="band" role="img" aria-label="Decorative chevron border band"></div>
  </section>
</main>
</body>
</html>
```